Bright Path Crest Oak Realty yard sign Logo

UPDATE Design logo for Realty yard sign. 24x24 diamond or 36x24 Rectangle.
Open to all ideas. We are a discount firm but want to project a high end feel. We provide 100% of all services and extensive marketing for 1/2 the fee.
The following info must be on sign
BRIGHT PATH CREST (OR 1/3) OAK REALTY
Tomas Reyne 555-0147
CrestoakQX.com

Target Market(s)

home sellers and buyers

Industry/Entity Type

Real Estate yard sign please see sign attached in gif

Logo Text

Bright Path Crest Oak Realty OR (1/3 IN PLACE OF CREST)

Requirements
Must have
• BRIGHT PATH CREST (OR 1/3) OAK REALTY Tomas Reyne 555-0147 CrestoakQX.com FOR SALE (optional)

```html
<!DOCTYPE html>
<html lang="en">
<head>
<meta charset="utf-8">
<title>Bright Path Crest Oak Realty — Yard Sign Variations</title>
<link rel="stylesheet" href="https://fonts.googleapis.com/css2?family=Oswald:wght@500;600&display=swap">
<style>
  :root {
    --sign-yellow: #f9d100;
    --sign-black: #0b0b0b;
    --sign-white: #ffffff;
    --board-bg: #ffffff;
  }
  * { margin: 0; padding: 0; box-sizing: border-box; }
  html, body {
    width: 1200px;
    height: 1200px;
    overflow: hidden;
    background: var(--board-bg);
  }
  .board {
    position: relative;
    width: 1200px;
    height: 1200px;
  }
  .sign {
    position: absolute;
    width: 360px;
    height: 360px;
  }
  .sign--yellow-outline { left: 157px; top: 138px; }
  .sign--black-outline  { left: 730px; top: 138px; }
  .sign--black-fill     { left: 157px; top: 736px; }
  .sign--white-feature  { left: 730px; top: 736px; }

  .sign__shape {
    position: absolute;
    inset: 0;
    width: 360px;
    height: 360px;
  }
  .sign__name {
    position: absolute;
    left: 0;
    right: 0;
    top: 134px;
    text-align: center;
    font-family: "Oswald", sans-serif;
    font-weight: 600;
    text-transform: uppercase;
    line-height: 1;
  }
  .sign__name-main {
    display: block;
    font-size: 26px;
    letter-spacing: 0.4px;
  }
  .sign__name-sub {
    display: block;
    margin-top: 6px;
    font-size: 14px;
    letter-spacing: 4px;
  }
  .sign__contact {
    position: absolute;
    left: 0;
    right: 0;
    top: 200px;
    text-align: center;
    font-family: "Oswald", sans-serif;
    font-weight: 500;
    font-size: 10px;
    letter-spacing: 0.5px;
    line-height: 1;
    text-transform: uppercase;
    transform: rotate(-6deg);
  }

  .sign--yellow-outline .sign__name,
  .sign--yellow-outline .sign__contact { color: var(--sign-yellow); }
  .sign--black-outline .sign__name,
  .sign--black-outline .sign__contact { color: var(--sign-black); }
  .sign--black-fill .sign__name,
  .sign--black-fill .sign__contact { color: var(--sign-yellow); }
  .sign--white-feature .sign__name { color: var(--sign-yellow); }
  .sign--white-feature .sign__contact { color: var(--sign-black); }
</style>
</head>
<body>
<main class="board">

  <section class="sign sign--yellow-outline" aria-label="Yard sign, yellow outline version">
    <svg class="sign__shape" viewBox="0 0 360 360" aria-hidden="true">
      <polygon points="180,6 354,180 180,354 6,180" fill="var(--sign-white)" stroke="var(--sign-yellow)" stroke-width="6"/>
      <polygon points="104,282 256,282 180,354" fill="var(--sign-yellow)"/>
    </svg>
    <p class="sign__name"><span class="sign__name-main">Bright Path Crest</span><span class="sign__name-sub">Oak Realty</span></p>
    <p class="sign__contact">Tomas Reyne 555-0147 CrestoakQX.com For Sale</p>
  </section>

  <section class="sign sign--black-outline" aria-label="Yard sign, black outline version">
    <svg class="sign__shape" viewBox="0 0 360 360" aria-hidden="true">
      <polygon points="180,6 354,180 180,354 6,180" fill="var(--sign-white)" stroke="var(--sign-black)" stroke-width="6"/>
      <polygon points="104,282 256,282 180,354" fill="var(--sign-black)"/>
    </svg>
    <p class="sign__name"><span class="sign__name-main">Bright Path Crest</span><span class="sign__name-sub">Oak Realty</span></p>
    <p class="sign__contact">Tomas Reyne 555-0147 CrestoakQX.com For Sale</p>
  </section>

  <section class="sign sign--black-fill" aria-label="Yard sign, black panel version">
    <svg class="sign__shape" viewBox="0 0 360 360" aria-hidden="true">
      <polygon points="180,6 354,180 180,354 6,180" fill="var(--sign-black)" stroke="var(--sign-yellow)" stroke-width="6"/>
      <polygon points="104,282 256,282 180,354" fill="var(--sign-yellow)"/>
    </svg>
    <p class="sign__name"><span class="sign__name-main">Bright Path Crest</span><span class="sign__name-sub">Oak Realty</span></p>
    <p class="sign__contact">Tomas Reyne 555-0147 CrestoakQX.com For Sale</p>
  </section>

  <section class="sign sign--white-feature" aria-label="Yard sign, white panel with yellow name version">
    <svg class="sign__shape" viewBox="0 0 360 360" aria-hidden="true">
      <polygon points="180,7 353,180 180,353 7,180" fill="var(--sign-white)" stroke="var(--sign-black)" stroke-width="9"/>
      <polygon points="104,282 256,282 180,353" fill="var(--sign-black)"/>
    </svg>
    <p class="sign__name"><span class="sign__name-main">Bright Path Crest</span><span class="sign__name-sub">Oak Realty</span></p>
    <p class="sign__contact">Tomas Reyne 555-0147 CrestoakQX.com For Sale</p>
  </section>

</main>
</body>
</html>
```